Velnix Orbit Nine Toothbrush Backcard Design

We need a toothbrush backcard (toothbrush packaging) design for our new toothbrush. We are one of the leading toothbrush distributor and producer company. At the moment our toothbrushes are selling at Varno, Sunpeak Shop, Q-Ninety and many more supermarkets and mom-and-pop shops in Thailand. Our toothbrush is emphasized on the soft and slim tip bristles which will not hurt your enamel. Easy to grip handle that will ease of use. These 2 mains point should be communicated through the design.

Our brand name is Velnix (see attached logo that you can use) and the toothbrush model is Orbit Nine. We will have 2 series for this model which are Orbit Nine Extra Soft and Orbit Nine Medium soft. They are basically differentiated by its packaging colors.

We are looking for the attractive and outstanding design from what available in the market right now. Please see enclosed die cut shape of the packaging. This backcard will hold 3 pieces of toothbrush with clear blister cover.

P.S We are very confident that our product produced with very good quality that's why we want to attract people to try. So when they walk in the aisle we want our toothbrush packaging to be eye catching and welcome customer to try.

Target Market(s)

B+ household consumers age between 18-65 both men and women who has open minded to the new product and willing to spend money without brand royalty.

Font styles to use
Sans Serif

Colors

Designer to choose colors to be used in the design.

Requirements
Must have
• - Logo, and model name
• - Quality mark as following GMP, KRV, ISO9001:2015, ISO22176
• - Attractive character which attract the target clients to try.
• - 2-sided packaging using attached die cut
Nice to have
Should not have
• What other brands have

```html
<!DOCTYPE html>
<html lang="en">
<head>
<meta charset="utf-8">
<title>Velnix Orbit Nine Backcard</title>
<link href="https://fonts.googleapis.com/css2?family=Poppins:wght@400;600;800&family=Dancing+Script:wght@600&display=swap" rel="stylesheet">
<style>
  :root{
    --teal:#17b6c8;
    --purple:#3d3b97;
    --yellow:#ffc20e;
    --red:#e3202c;
    --orange:#f26522;
    --white:#ffffff;
    --badge:#3a3a3a;
    --mint:#8fe0cf;
  }
  html,body{margin:0;padding:0;overflow:hidden;}
  body{width:961px;height:1200px;background:var(--white);position:relative;font-family:"Poppins",sans-serif;}
  .card{position:absolute;top:122px;width:311px;height:976px;overflow:hidden;border-radius:42px;}
  .card--front{left:150px;}
  .card--back{left:513px;}
  .card__bg{position:absolute;inset:0;}
  .abs{position:absolute;}
  .logo{font-weight:800;color:var(--white);letter-spacing:0.5px;display:flex;align-items:center;gap:4px;line-height:1;}
  .logo__dot{width:9px;height:9px;border-radius:50%;background:var(--yellow);}
  .logo--small{font-size:22px;}
  .model{transform-origin:left top;transform:rotate(-90deg);display:flex;align-items:center;gap:4px;white-space:nowrap;line-height:1;}
  .model__name{font-size:18px;font-weight:600;color:var(--yellow);}
  .model__tag{font-size:7px;font-weight:800;background:var(--yellow);color:var(--purple);padding:1px 4px;border-radius:8px;}
  .model__soft{font-family:"Dancing Script",cursive;font-size:24px;color:var(--yellow);}
  .badge{background:var(--badge);border-radius:3px;}
  .badge--round{border-radius:50%;}
  .brush-art{border-radius:30px;background:linear-gradient(180deg,#f4f6f8 0%,#eef1f3 35%,var(--mint) 60%,#e8f7f3 100%);}
  .ribbon{transform-origin:center;background:linear-gradient(90deg,var(--red),var(--orange));color:var(--white);font-weight:800;text-align:center;line-height:1.1;padding:6px 14px;border-radius:0 30px 0 30px;}
  .pack{width:120px;height:120px;background:var(--red);transform:rotate(45deg);border:3px solid var(--white);}
  .pack__text{text-align:center;color:var(--white);line-height:1;}
  .pack__num{font-size:46px;font-weight:800;}
  .pack__premium{font-size:13px;font-weight:600;color:var(--yellow);}
  .pack__soft{font-family:"Dancing Script",cursive;font-size:18px;color:var(--yellow);}
  .pack__tag{font-size:6px;font-weight:800;background:var(--yellow);color:var(--purple);padding:1px 4px;border-radius:6px;}
  .pack__label{font-size:20px;font-weight:800;}
  .big-logo{transform-origin:left top;transform:rotate(-90deg);font-size:66px;font-weight:800;color:var(--white);white-space:nowrap;display:flex;align-items:center;gap:8px;line-height:1;}
  .big-logo .logo__dot{width:18px;height:18px;}
  .extra-tag{background:var(--yellow);color:var(--purple);font-weight:800;font-size:14px;padding:2px 12px;border-radius:12px;}
  .info{border:1px solid rgba(255,255,255,0.45);border-radius:6px;color:var(--white);font-size:8.5px;line-height:1.45;text-align:center;padding:10px 12px;box-sizing:border-box;}
  .info p{margin:0 0 14px;}
  .badge-row{display:flex;gap:10px;align-items:center;background:var(--white);padding:3px 6px;box-sizing:border-box;}
  .badge-row .badge{height:20px;}
  .label-panel{background:var(--white);}
</style>
</head>
<body>

<section class="card card--front">
  <svg class="card__bg" width="311" height="976" viewBox="0 0 311 976">
    <defs>
      <radialGradient id="burstF" cx="0.55" cy="0.35" r="0.7">
        <stop offset="0" stop-color="#ffffff"/><stop offset="1" stop-color="#c9ced4"/>
      </radialGradient>
    </defs>
    <rect width="311" height="976" fill="var(--teal)"/>
    <path d="M0 300 Q150 170 311 150 L311 976 L0 976Z" fill="url(#burstF)" role="img" aria-label="Soft radiating light burst behind the brushes"/>
    <path d="M0 300 Q150 170 311 150" fill="none" stroke="var(--yellow)" stroke-width="9"/>
    <path d="M0 590 Q160 470 311 420 L311 976 L0 976Z" fill="var(--purple)"/>
    <rect x="22" y="28" width="267" height="930" rx="26" fill="none" stroke="rgba(255,255,255,0.5)" stroke-width="1"/>
    <rect x="120" y="68" width="135" height="52" rx="10" fill="none" stroke="rgba(255,255,255,0.6)" stroke-width="1.2"/>
  </svg>

  <div class="abs logo logo--small" style="left:58px;top:40px;">Velnix<span class="logo__dot"></span></div>
  <div class="abs model" style="left:32px;top:240px;"><span class="model__name">Orbit Nine</span><span class="model__tag">EXTRA</span><span class="model__soft">Soft</span></div>

  <div class="abs badge" style="left:30px;top:252px;width:22px;height:38px;"></div>
  <div class="abs badge" style="left:30px;top:305px;width:22px;height:60px;"></div>
  <div class="abs badge badge--round" style="left:31px;top:376px;width:20px;height:20px;"></div>
  <div class="abs badge" style="left:30px;top:410px;width:22px;height:38px;"></div>

  <div class="abs brush-art" style="left:95px;top:178px;width:195px;height:755px;" role="img" aria-label="Three white toothbrushes with mint green grip handles"></div>

  <div class="abs ribbon" style="left:-20px;top:485px;width:180px;font-size:13px;transform:rotate(-62deg);">Soft &amp; Slim Tip Bristles<br><span style="font-size:17px;">Easy to Grip</span></div>

  <div class="abs big-logo" style="left:24px;top:906px;">Velnix<span class="logo__dot"></span></div>
  <div class="abs extra-tag" style="left:30px;top:918px;">EXTRA</div>

  <div class="abs pack" style="left:135px;top:713px;"></div>
  <div class="abs pack__text" style="left:125px;top:705px;width:140px;">
    <div class="pack__num">3</div>
    <div class="pack__premium">Orbit Nine</div>
    <div><span class="pack__tag">EXTRA</span> <span class="pack__soft">Soft</span></div>
    <div class="pack__label">PACK</div>
  </div>
</section>

<section class="card card--back">
  <svg class="card__bg" width="311" height="976" viewBox="0 0 311 976">
    <defs>
      <radialGradient id="burstB" cx="0.35" cy="0.4" r="0.7">
        <stop offset="0" stop-color="#ffffff"/><stop offset="1" stop-color="#c9ced4"/>
      </radialGradient>
    </defs>
    <rect width="311" height="976" fill="var(--teal)"/>
    <path d="M0 260 Q130 190 311 150 L311 976 L0 976Z" fill="url(#burstB)" role="img" aria-label="Soft radiating light burst behind the brushes"/>
    <path d="M0 260 Q130 190 311 150" fill="none" stroke="var(--yellow)" stroke-width="8"/>
    <path d="M0 590 Q160 500 311 430 L311 976 L0 976Z" fill="var(--purple)"/>
    <path d="M0 590 Q160 500 311 430" fill="none" stroke="var(--yellow)" stroke-width="8"/>
    <rect x="22" y="28" width="267" height="930" rx="26" fill="none" stroke="rgba(255,255,255,0.5)" stroke-width="1"/>
    <rect x="16" y="68" width="175" height="52" rx="10" fill="none" stroke="rgba(255,255,255,0.6)" stroke-width="1.2"/>
  </svg>

  <div class="abs logo logo--small" style="left:62px;top:155px;">Velnix<span class="logo__dot"></span></div>
  <div class="abs model" style="left:222px;top:200px;"><span class="model__name">Orbit Nine</span><span class="model__tag">EXTRA</span><span class="model__soft">Soft</span></div>

  <div class="abs brush-art" style="left:50px;top:215px;width:218px;height:305px;" role="img" aria-label="Three white toothbrushes with mint green grips shown at an angle"></div>

  <div class="abs ribbon" style="left:20px;top:420px;width:110px;font-size:9px;transform:rotate(-62deg);">Soft &amp; Slim Tip Bristles<br><span style="font-size:12px;">Easy to Grip</span></div>

  <div class="abs pack" style="left:98px;top:488px;width:100px;height:100px;"></div>
  <div class="abs pack__text" style="left:88px;top:485px;width:120px;">
    <div class="pack__num" style="font-size:38px;">3</div>
    <div class="pack__premium" style="font-size:11px;">Orbit Nine</div>
    <div><span class="pack__tag">EXTRA</span> <span class="pack__soft" style="font-size:15px;">Soft</span></div>
    <div class="pack__label" style="font-size:16px;">PACK</div>
  </div>

  <div class="abs logo" style="left:90px;top:622px;font-size:25px;">Velnix<span class="logo__dot"></span></div>

  <div class="abs info" style="left:52px;top:664px;width:205px;height:166px;">
    <p>Manufactured and marketed by Velnix Co., Ltd.</p>
    <p>88 Rama Road, Bang Na, Bangkok 10260 Thailand. Made in Thailand for home use.</p>
  </div>

  <div class="abs badge-row" style="left:52px;top:835px;width:205px;height:28px;">
    <div class="badge" style="width:38px;"></div>
    <div class="badge badge--round" style="width:20px;"></div>
    <div class="badge" style="width:58px;"></div>
    <div class="badge" style="width:38px;"></div>
  </div>
  <div class="abs label-panel" style="left:52px;top:870px;width:205px;height:74px;"></div>
</section>

</body>
</html>
```